business card design for luxurious real estate brand

using the attached logo, i am looking for a 2-sided business card design. the back should be the gold logo on black background. the front needs to include: gold logo, name, phone, email, and website

Industry/Entity Type

real estate

Contact Information for Business Card

logo, name, email, phone, website

Font styles to use
Sans Serif

```html
<!DOCTYPE html>
<html lang="en">
<head>
<meta charset="utf-8">
<title>Orlane Homes — Business Card</title>
<link rel="stylesheet" href="https://fonts.googleapis.com/css2?family=Barlow:wght@400;500;600&display=swap">
<style>
  :root {
    --page: #cbcbcb;
    --card: #000000;
    --gold: #ffcc0a;
    --ink: #ffffff;
  }
  * { box-sizing: border-box; margin: 0; padding: 0; }
  html, body {
    width: 1200px; height: 1200px; overflow: hidden;
    background: var(--page);
    font-family: "Barlow", Arial, sans-serif;
  }
  .card {
    position: absolute; left: 170px;
    width: 860px; height: 503px;
    background: var(--card);
    overflow: hidden;
  }
  .card--front { top: 76px; }
  .card--back { top: 627px; }
  .band { position: absolute; left: 0; top: 0; width: 860px; height: 503px; }
  .band polygon { fill: var(--gold); }

  .brand {
    position: absolute; display: flex; align-items: center; gap: 12px;
    color: var(--gold); font-weight: 500; font-size: 28px;
    letter-spacing: 0.14em; white-space: nowrap;
  }
  .brand__mark { width: 14px; height: 14px; background: var(--gold); flex: none; }
  .card--front .brand { left: 215px; top: 250px; transform: translate(-50%, -50%); }
  .card--back .brand { left: 430px; top: 225px; transform: translate(-50%, -50%); }

  .divider {
    position: absolute; left: 429px; top: 70px;
    width: 2px; height: 362px; background: var(--gold);
  }
  .person { position: absolute; left: 484px; top: 150px; }
  .person__name { font-size: 35px; font-weight: 600; color: var(--ink); line-height: 1; }
  .person__first { color: var(--gold); }
  .person__role { margin-top: 8px; font-size: 21px; color: var(--ink); letter-spacing: 0.02em; }

  .contacts { position: absolute; left: 490px; top: 312px; list-style: none; }
  .contacts li {
    display: flex; align-items: center; gap: 10px;
    height: 25px; margin-bottom: 15px;
    font-size: 21px; color: var(--ink);
  }
  .contacts svg { width: 14px; height: 14px; fill: var(--ink); flex: none; }
  .accent { color: var(--gold); }

  .web-back {
    position: absolute; left: 500px; top: 412px;
    font-size: 21px; color: var(--ink);
  }
</style>
</head>
<body>

<section class="card card--front" aria-label="Card front">
  <svg class="band" viewBox="0 0 860 503" aria-hidden="true">
    <polygon points="668,0 726,0 860,226 860,330"/>
  </svg>
  <div class="brand"><span class="brand__mark"></span>ORLANE HOMES</div>
  <div class="divider"></div>
  <div class="person">
    <p class="person__name"><span class="person__first">Theo</span> Hartwell</p>
    <p class="person__role">Owner / Founder</p>
  </div>
  <ul class="contacts">
    <li>
      <svg viewBox="0 0 24 24" aria-hidden="true"><path d="M6.6 10.8a15 15 0 0 0 6.6 6.6l2.2-2.2a1 1 0 0 1 1-.25 11.4 11.4 0 0 0 3.6.57 1 1 0 0 1 1 1V20a1 1 0 0 1-1 1A17 17 0 0 1 3 4a1 1 0 0 1 1-1h3.5a1 1 0 0 1 1 1c0 1.25.2 2.45.57 3.6a1 1 0 0 1-.25 1z"/></svg>
      555-014-2280 ext. 118
    </li>
    <li>
      <svg viewBox="0 0 24 24" aria-hidden="true"><path d="M2 5h20v14H2z M3.5 6.5 12 13l8.5-6.5" fill="var(--ink)" stroke="var(--card)" stroke-width="1.6"/></svg>
      theo@hartwellbuild.ca
    </li>
    <li>
      <svg viewBox="0 0 24 24" aria-hidden="true"><circle cx="12" cy="12" r="10"/><path d="M2 12h20M12 2c3 3.5 3 16.5 0 20M12 2c-3 3.5-3 16.5 0 20" fill="none" stroke="var(--card)" stroke-width="1.5"/></svg>
      <span>www.<span class="accent">hartwellbuilders</span>.ca</span>
    </li>
  </ul>
</section>

<section class="card card--back" aria-label="Card back">
  <svg class="band" viewBox="0 0 860 503" aria-hidden="true">
    <polygon points="0,45 0,135 248,503 312,503"/>
  </svg>
  <div class="brand"><span class="brand__mark"></span>ORLANE HOMES</div>
  <p class="web-back">www.<span class="accent">hartwellbuilders</span>.ca</p>
</section>

</body>
</html>
```